Security doors and flyscreens

We need business cards for our company called K & M Distributors. We quote, manufacture and install security doors and flyscreens.

Industry/Entity Type

Security

Contact Information for Business Card

K & M DISTRIBUTORS
17 Larkvale Rd. Ashbrook 3089
Ph: 8157 2604
Fax: 8157 2609
Gavin: 0419 275 916
Email: gatesupplier@mailbox-example.net

```html
<!DOCTYPE html>
<html lang="en">
<head>
<meta charset="utf-8">
<title>K &amp; M Distributors – Business Card</title>
<link rel="stylesheet" href="https://fonts.googleapis.com/css2?family=Questrial&display=swap">
<style>
  :root {
    --backdrop: #d9dfdf;
    --card: #ffffff;
    --ink: #2b2d2f;
    --grey-text: #5a5e62;
    --orange: #f47a1f;
    --cyan: #5fd8dc;
    --divider: #b9bcbf;
  }
  * { margin: 0; padding: 0; box-sizing: border-box; }
  html, body {
    width: 1200px;
    height: 676px;
    overflow: hidden;
    background: var(--backdrop);
  }
  .card {
    position: absolute;
    left: 150px;
    top: 81px;
    width: 900px;
    height: 514px;
    background: var(--card);
    overflow: hidden;
    box-shadow: 0 8px 28px rgba(0,0,0,0.12);
    font-family: "Questrial", "Century Gothic", sans-serif;
  }
  .brand {
    position: absolute;
    left: 52px;
    top: 120px;
    width: 290px;
    color: var(--ink);
    font-weight: 400;
    line-height: 1;
  }
  .brand-mark {
    display: inline-block;
    width: 34px;
    height: 34px;
    background: var(--orange);
    vertical-align: middle;
    margin-right: 14px;
  }
  .brand-initials {
    font-size: 74px;
    vertical-align: middle;
  }
  .brand-word {
    display: block;
    font-size: 44px;
    margin-top: 14px;
  }
  .divider {
    position: absolute;
    left: 360px;
    top: 96px;
    width: 2px;
    height: 196px;
    background: var(--divider);
  }
  .contact {
    position: absolute;
    left: 384px;
    top: 92px;
    right: 20px;
  }
  .address {
    color: var(--orange);
    font-size: 36px;
    line-height: 1.08;
    letter-spacing: 1px;
    margin-bottom: 22px;
  }
  .contact-line {
    font-size: 23px;
    line-height: 1.42;
    color: var(--grey-text);
    letter-spacing: 0.5px;
  }
  .contact-label { color: var(--cyan); }
  .bands {
    position: absolute;
    left: 0;
    bottom: 0;
    width: 900px;
    height: 120px;
  }
</style>
</head>
<body>
  <div class="card">
    <div class="brand">
      <span class="brand-mark"></span><span class="brand-initials">K &amp; M</span>
      <span class="brand-word">Distributors</span>
    </div>

    <div class="divider"></div>

    <div class="contact">
      <p class="address">17 Larkvale Rd.<br>Ashbrook 3089</p>
      <p class="contact-line"><span class="contact-label">Gavin:</span> 0419 275 916</p>
      <p class="contact-line"><span class="contact-label">Ph:</span> 8157 2604</p>
      <p class="contact-line"><span class="contact-label">Fax:</span> 8157 2609</p>
      <p class="contact-line"><span class="contact-label">Email:</span> gatesupplier@mailbox-example.net</p>
    </div>

    <svg class="bands" viewBox="0 0 900 120" aria-hidden="true">
      <polygon points="0,8 420,22 436,34 0,20" fill="var(--cyan)"/>
      <polygon points="0,26 436,40 456,52 900,62 900,120 0,120" fill="var(--orange)"/>
    </svg>
  </div>
</body>
</html>
```